Ridgeline Journeys business card

please see website
www.ridgelinejourneys.comau

info needed on card
Kieran Folsby
Ph
email
Adventure Riding GPS trails

please use my logo and colours off my site

Industry/Entity Type

Business

Contact Information for Business Card

Kieran Folsby
kieran@ridgelinejourneys.com

```html
<!DOCTYPE html>
<html lang="en">
<head>
<meta charset="utf-8">
<title>Ridgeline Journeys – Business Card</title>
<link rel="stylesheet" href="https://fonts.googleapis.com/css2?family=Tinos:wght@400;700&display=swap">
<style>
  :root {
    --canvas-bg: #e9e6e0;
    --card-yellow: #f2c83c;
    --card-black: #0b0b0b;
    --frame-grey: #6b6b6b;
    --ink: #1a1a1a;
    --ring-grey: #6e6e6e;
  }
  * { margin: 0; padding: 0; box-sizing: border-box; }
  html, body {
    width: 1200px; height: 1000px; overflow: hidden;
    background: var(--canvas-bg);
  }
  .canvas {
    width: 1200px; height: 1000px;
    display: flex; flex-direction: column; align-items: center; justify-content: center;
    gap: 60px;
  }
  .card {
    width: 700px; height: 400px; position: relative;
    box-shadow: 0 6px 18px rgba(0,0,0,.18);
  }
  .card-front {
    background: var(--card-yellow);
    font-family: "Tinos", "Times New Roman", serif;
    color: var(--ink);
  }
  .front-frame {
    position: absolute; inset: 28px;
    border: 4px solid var(--frame-grey);
  }
  .holder-name {
    position: absolute; left: 70px; top: 60px;
    font-size: 48px; font-weight: 400; letter-spacing: 2px;
  }
  .brand {
    position: absolute; left: 70px; top: 170px;
    display: flex; align-items: center; gap: 18px;
  }
  .brand-mark {
    width: 56px; height: 56px; border-radius: 50%;
    background: var(--ink);
  }
  .brand-name {
    font-size: 34px; font-weight: 700; text-transform: uppercase;
    line-height: 1.05; letter-spacing: 1px;
  }
  .contact {
    position: absolute; display: flex; align-items: center; gap: 10px;
    font-size: 22px;
  }
  .contact svg { width: 22px; height: 22px; fill: var(--ink); flex: none; }
  .contact-phone { left: 430px; top: 250px; }
  .contact-email { left: 70px; top: 310px; }
  .card-back { background: var(--card-black); overflow: hidden; }
  .back-pattern {
    position: absolute; inset: 0;
    background: radial-gradient(circle at 50% 50%, #3a3a3a 0%, #202020 38%, var(--card-black) 70%);
  }
</style>
</head>
<body>
<main class="canvas">
  <section class="card card-front" aria-label="Business card front">
    <div class="front-frame"></div>
    <h1 class="holder-name">Kieran Folsby</h1>
    <div class="brand">
      <span class="brand-mark"></span>
      <span class="brand-name">Ridgeline<br>Journeys</span>
    </div>
    <p class="contact contact-phone">
      <svg viewBox="0 0 24 24" aria-hidden="true"><path d="M6.6 10.8a15 15 0 0 0 6.6 6.6l2.2-2.2c.3-.3.7-.4 1-.2 1.1.4 2.3.6 3.6.6.6 0 1 .4 1 1V20c0 .6-.4 1-1 1A17 17 0 0 1 3 4c0-.6.4-1 1-1h3.5c.6 0 1 .4 1 1 0 1.3.2 2.5.6 3.6.1.3 0 .7-.2 1z"/></svg>
      0198-765-432
    </p>
    <p class="contact contact-email">
      <svg viewBox="0 0 24 24" aria-hidden="true"><path d="M2 5h20v14H2zM3.5 6.5v.4L12 13l8.5-6.1v-.4z"/></svg>
      kieran@ridgelinejourneys.com
    </p>
  </section>

  <section class="card card-back" aria-label="Business card back">
    <div class="back-pattern" role="img" aria-label="Large grey dashed ring decoration on black"></div>
  </section>
</main>
</body>
</html>
```